Harlow Ridge Growers and Nursery needs a business street sign.

I have three businesses located at the same address: The Harlow Ridge Growers & Nursery, The Bramble Nook, and The Quarry Commons. I am looking for a 4’ x 8’ street sign to represent all three businesses as one retail experience. It needs to be eye catching yet simple enough that people can fully read it while driving by. I have logos for the greenhouse and village however I do not have anything for The Bramble Nook. I’m looking for some type of font that’s similar or in between the two attached logos for The Bramble Nook.

• Horizontal Sign, Eye catching, yet simple design so people see it while driving by.
• Horizontal Sign
• I’m open to the design being both vertical and horizontal. Please provide both options

```html
<!DOCTYPE html>
<html lang="en">
<head>
<meta charset="utf-8">
<title>Harlow Ridge Growers &amp; Nursery – Street Sign Options</title>
<link rel="stylesheet" href="https://fonts.googleapis.com/css2?family=Open+Sans:wght@400;600;700&display=swap">
<style>
  :root {
    --green: #026a3f;
    --maroon: #7f2322;
    --slate: #2c2f3a;
    --white: #ffffff;
    --paper: #ffffff;
  }
  * { margin: 0; padding: 0; box-sizing: border-box; }
  html, body { width: 798px; height: 1200px; overflow: hidden; background: var(--paper); }
  body { position: relative; font-family: "Open Sans", Arial, sans-serif; }

  .sign { position: absolute; box-shadow: 0 1px 5px rgba(0,0,0,.25); overflow: hidden; }

  .panel { position: absolute; left: 0; width: 100%; display: flex; align-items: center; justify-content: center; }

  /* vertical option */
  .sign--vertical { left: 239px; top: 80px; width: 320px; height: 638px; }
  .sign--vertical .panel--nursery { top: 0; height: 223px; background: var(--green); }
  .sign--vertical .panel--commons { top: 223px; height: 192px; }
  .sign--vertical .panel--nook { top: 415px; height: 223px; }

  /* horizontal option */
  .sign--horizontal { left: 80px; top: 796px; width: 638px; height: 320px; }
  .sign--horizontal .panel--nursery { left: 0; top: 0; width: 325px; height: 249px; background: var(--white); }
  .sign--horizontal .panel--commons { left: 325px; top: 0; width: 313px; height: 162px; }
  .sign--horizontal .panel--nook { left: 325px; top: 162px; width: 313px; height: 158px; }

  .available {
    position: absolute; left: 0; top: 249px; width: 325px; height: 71px;
    background: var(--maroon); color: var(--white);
    font-weight: 700; font-size: 34px; letter-spacing: .3px;
    display: flex; align-items: center; justify-content: center;
  }

  .photo { position: absolute; inset: 0; }
  .photo--grass-light { background: linear-gradient(180deg, #dcdddb 0%, #e9eae6 45%, #c9cfc2 80%, #9aa592 100%); }
  .photo--grass-green { background: linear-gradient(180deg, #b8cf9c 0%, #c7dcae 50%, #a9c48a 100%); }
  .photo--blooms {
    background:
      radial-gradient(ellipse at 75% 80%, #4a2f3a 0%, rgba(74,47,58,0) 55%),
      radial-gradient(ellipse at 60% 20%, #3d3a4a 0%, rgba(61,58,74,0) 50%),
      var(--slate);
  }

  .name { position: relative; font-weight: 700; text-align: center; line-height: 1.15; }
  .name--nursery { color: var(--white); font-size: 31px; }
  .name--nursery-dark { color: var(--green); font-size: 30px; }
  .name--commons { color: var(--maroon); font-size: 40px; }
  .sign--horizontal .name--commons { font-size: 36px; }
  .name--nook { color: var(--white); font-weight: 600; font-size: 38px; }
  .sign--horizontal .name--nook { font-size: 34px; }
</style>
</head>
<body>

<section class="sign sign--vertical" aria-label="Vertical sign option">
  <div class="panel panel--nursery">
    <p class="name name--nursery">The Harlow Ridge<br>Growers &amp; Nursery</p>
  </div>
  <div class="panel panel--commons">
    <div class="photo photo--grass-light" role="img" aria-label="Soft-focus photo of grass in pale morning light"></div>
    <p class="name name--commons">Quarry<br>Commons</p>
  </div>
  <div class="panel panel--nook">
    <div class="photo photo--blooms" role="img" aria-label="Dark moody photo of flower petals"></div>
    <p class="name name--nook">The Bramble<br>Nook</p>
  </div>
</section>

<section class="sign sign--horizontal" aria-label="Horizontal sign option">
  <div class="panel panel--nursery">
    <p class="name name--nursery-dark">The Harlow Ridge<br>Growers &amp; Nursery</p>
  </div>
  <div class="available">AVAILABLE HERE</div>
  <div class="panel panel--commons">
    <div class="photo photo--grass-green" role="img" aria-label="Soft-focus photo of green grass"></div>
    <p class="name name--commons">Quarry<br>Commons</p>
  </div>
  <div class="panel panel--nook">
    <div class="photo photo--blooms" role="img" aria-label="Dark moody photo of flower petals"></div>
    <p class="name name--nook">The Bramble<br>Nook</p>
  </div>
</section>

</body>
</html>
```